Business Card - Cooperate

Business Card for Larkfield Management Consulting

Target Market(s)

Corparte - b2B

Industry/Entity Type

Management Consulting - Professional Services

Contact Information for Business Card

Company Name , Slogan , Dummy Address,

Requirements
Must have
• Reach your Full Potential

```html
<!DOCTYPE html>
<html lang="en">
<head>
<meta charset="utf-8">
<title>Larkfield Management Consulting – Business Card</title>
<link href="https://fonts.googleapis.com/css2?family=Montserrat:wght@500;600;700;800&display=swap" rel="stylesheet">
<style>
  :root {
    --page-bg: #e9e7e3;
    --card-bg: #ffffff;
    --brand-blue: #2a4fc4;
    --deep-blue: #2d3a9c;
    --sky-blue: #2aa8e0;
    --leaf-green: #5cc72c;
    --teal: #1f9e8a;
    --ink: #2a2a2e;
    --shadow: rgba(40, 30, 20, 0.18);
  }
  * { box-sizing: border-box; margin: 0; padding: 0; }
  html, body { width: 1200px; height: 913px; overflow: hidden; }
  body {
    background: var(--page-bg);
    font-family: "Montserrat", sans-serif;
    position: relative;
  }
  .card {
    position: absolute;
    width: 525px;
    height: 300px;
    background: var(--card-bg);
    box-shadow: 0 10px 28px var(--shadow);
    overflow: hidden;
  }
  .card--front { left: 70px; top: 110px; }
  .card--back  { left: 605px; top: 500px; }

  .wordmark {
    display: flex;
    align-items: center;
    gap: 12px;
  }
  .wordmark__dot {
    border-radius: 50%;
    background: var(--brand-blue);
    flex: none;
  }
  .wordmark__name {
    font-weight: 700;
    color: var(--brand-blue);
    letter-spacing: 0.5px;
    line-height: 1;
  }
  .tagline {
    font-weight: 700;
    color: var(--teal);
    text-transform: uppercase;
    letter-spacing: 2.4px;
  }

  /* front */
  .card--front .wordmark { position: absolute; left: 42px; bottom: 62px; }
  .card--front .wordmark__dot { width: 44px; height: 44px; }
  .card--front .wordmark__name { font-size: 46px; }
  .card--front .tagline { position: absolute; left: 100px; bottom: 40px; font-size: 10.5px; }

  /* back */
  .card--back .wordmark { position: absolute; left: 36px; top: 34px; }
  .card--back .wordmark__dot { width: 40px; height: 40px; }
  .card--back .wordmark__name { font-size: 38px; }
  .card--back .tagline { position: absolute; left: 90px; top: 82px; font-size: 8.5px; letter-spacing: 2px; }

  .rule { position: absolute; left: 0; top: 0; }

  .person { position: absolute; left: 36px; top: 128px; }
  .person__name { font-size: 19px; font-weight: 800; color: var(--ink); }
  .person__role { font-size: 14px; font-weight: 700; color: var(--brand-blue); margin-top: 1px; }

  .contacts { position: absolute; left: 36px; top: 188px; list-style: none; }
  .contacts li {
    display: flex; align-items: center; gap: 9px;
    font-size: 12px; font-weight: 600; color: var(--ink);
    margin-bottom: 6px;
  }
  .contacts svg { width: 14px; height: 14px; flex: none; }

  .address {
    position: absolute; right: 40px; top: 108px;
    font-size: 11px; font-weight: 500; color: var(--ink);
    line-height: 1.35; text-align: left;
  }
  .band { position: absolute; left: 0; bottom: 0; }
</style>
</head>
<body>

<section class="card card--front" aria-label="Business card front">
  <div class="wordmark">
    <span class="wordmark__dot"></span>
    <span class="wordmark__name">Larkfield</span>
  </div>
  <p class="tagline">Reach your full potential</p>
</section>

<section class="card card--back" aria-label="Business card back">
  <svg class="rule" width="525" height="300" viewBox="0 0 525 300" aria-hidden="true">
    <defs>
      <linearGradient id="ruleGrad" x1="0" x2="1" y1="0" y2="0">
        <stop offset="0" stop-color="#5cc72c"/>
        <stop offset="0.5" stop-color="#2d3a9c"/>
        <stop offset="1" stop-color="#2aa8e0"/>
      </linearGradient>
    </defs>
    <line x1="205" y1="140" x2="360" y2="140" stroke="url(#ruleGrad)" stroke-width="1.6"/>
    <line x1="330" y1="96" x2="495" y2="96" stroke="url(#ruleGrad)" stroke-width="1.6"/>
  </svg>

  <div class="wordmark">
    <span class="wordmark__dot"></span>
    <span class="wordmark__name">Larkfield</span>
  </div>
  <p class="tagline">Reach your full potential</p>

  <div class="person">
    <p class="person__name">Daniel Whitaker</p>
    <p class="person__role">CEO/FOUNDER</p>
  </div>

  <ul class="contacts">
    <li>
      <svg viewBox="0 0 16 16" aria-hidden="true"><path d="M3 1.5l3 3-1.6 1.8a9 9 0 005.3 5.3L11.5 10l3 3-1.8 2A12 12 0 011 3.3z" fill="var(--deep-blue)"/></svg>
      (555) 014-2273
    </li>
    <li>
      <svg viewBox="0 0 16 16" aria-hidden="true"><rect x="1" y="3" width="14" height="10" fill="var(--brand-blue)"/><path d="M1 3l7 6 7-6" fill="none" stroke="#fff" stroke-width="1.3"/></svg>
      daniel@larkfieldgroup.com
    </li>
    <li>
      <svg viewBox="0 0 16 16" aria-hidden="true"><circle cx="8" cy="8" r="6.5" fill="none" stroke="var(--deep-blue)" stroke-width="1.4"/><ellipse cx="8" cy="8" rx="2.8" ry="6.5" fill="none" stroke="var(--deep-blue)" stroke-width="1.1"/><path d="M1.5 8h13M2.5 5h11M2.5 11h11" stroke="var(--deep-blue)" stroke-width="1"/></svg>
      www.larkfieldgroup.com
    </li>
  </ul>

  <p class="address">418 Alder Court Suite 12<br>Fremont,<br>CA 94538</p>

  <svg class="band" width="525" height="60" viewBox="0 0 525 60" aria-hidden="true">
    <defs>
      <linearGradient id="bandGrad" x1="0" x2="1" y1="0" y2="0">
        <stop offset="0" stop-color="#5cc72c"/>
        <stop offset="0.45" stop-color="#2a4fc4"/>
        <stop offset="0.75" stop-color="#2d3a9c"/>
        <stop offset="1" stop-color="#2aa8e0"/>
      </linearGradient>
    </defs>
    <path d="M0 42 L420 42 L440 18 L525 18 L525 60 L0 60 Z" fill="url(#bandGrad)"/>
    <path d="M0 38 L418 38 L438 14 L525 14 L525 16 L439 16 L419 40 L0 40 Z" fill="var(--deep-blue)"/>
  </svg>
</section>

</body>
</html>
```